An expert for Professional and Technical Evaluation of Painting Work Needs a New Letterhead Design

I own a mid-sized painting company and also work as an expert for professional and technical evaluation of painting work in the area of Zurich.

Please read the project description and the must-have-requirements carefully!

I attached 1 PDF which will help you create a new letterhead design:

THE NEW DESIGN DOESN'T NEED A LOGO! (Because it won't represent a company, it represents only a service)
Updates

Dear designers We had a discussion about the location/placement of the design and came to the conclusion that we only want the design to be in the header area of the A4-paper. We would be glad to receive some revised version of your designs. Thank you and kind regards!

Project Deadline Extended
Reason: Due to the fact that only 20% of the designer have understood the brief and submitted designs that have met the requirements we decided to extend the contest deadline.

Project Deadline Extended
Reason: A great deal of good designs were submitted in the last few days. A big thank you to all the participating designers for your good work. We need a few more days to discuss some changes with certain designers and to decide which design will win.

Target Market(s)

(Insurance) Companies, partly also private clients.

Industry/Entity Type

Painting

Colors

Designer to choose colors to be used in the design.

Requirements
Must have
• All information (text, phone numbers, ...) of the old design ("old_letterhead_design.pdf") has also to be in the new one. Additional to that there are a few changes:
The phone numbers "01 583 61 47" and "01 583 61 37" change to "044 583 61 47" and "044 583 61 37". And please mention also this email address: gutachten@valmorkeller.example .

- The design should only be in the header-area of the A4-paper. An the background color of the A4-paper will be white.

- The design should consist of two designs. One for the first page and a smaller version of the design for the following pages.

- THE NEW DESIGN DOESN'T NEED A LOGO! You can make a design with geometric forms, ...

- The new design should have a juridical look. It should only contain colors like brown, fawn, black, light green, ...... colors which look serious/reliable.
Nice to have
• Geometric Forms, Symbols or other design elements.

- It would also be nice to have some design elements which emphasize the kind of work we are offering.

```html
<!DOCTYPE html>
<html lang="de">
<head>
<meta charset="utf-8">
<title>Valmor Keller – Briefpapier</title>
<link href="https://fonts.googleapis.com/css2?family=Questrial&display=swap" rel="stylesheet">
<style>
  :root {
    --backdrop: #ececec;
    --paper: #fbfbfb;
    --violet: #6d558f;
    --slate: #9c9c9c;
    --ink: #4a4a4a;
    --white: #ffffff;
  }
  * { margin: 0; padding: 0; box-sizing: border-box; }
  html, body { width: 1200px; height: 815px; overflow: hidden; }
  body {
    background: var(--backdrop);
    font-family: "Questrial", "Century Gothic", sans-serif;
    position: relative;
  }
  .sheet {
    position: absolute;
    top: 70px;
    width: 482px;
    height: 683px;
    background: var(--paper);
    overflow: hidden;
  }
  .sheet--first { left: 80px; }
  .sheet--follow { left: 638px; }

  /* first page header */
  .name-band {
    position: absolute;
    left: 0; top: 0;
    width: 288px; height: 78px;
    background: var(--violet);
    clip-path: polygon(0 0, 100% 0, 91.3% 100%, 0 100%);
    color: var(--white);
    padding: 34px 0 0 23px;
  }
  .name-band__name { font-size: 14px; letter-spacing: 0.2px; line-height: 1; }
  .name-band__title { font-size: 9.5px; margin-top: 3px; line-height: 1; }

  .contact-band {
    position: absolute;
    left: 264px; top: 20px;
    width: 218px; height: 58px;
    background: var(--slate);
    clip-path: polygon(20px 0, 100% 0, 100% 100%, 0 100%);
    color: #dedede;
    font-size: 6.2px;
    line-height: 8.4px;
    text-align: right;
    padding: 16px 21px 0 0;
    white-space: nowrap;
  }
  .contact-band b { color: var(--white); font-weight: normal; }

  .services {
    position: absolute;
    left: 23px; top: 92px;
    width: 438px;
    font-size: 9px;
    line-height: 12px;
    color: var(--ink);
    text-align: justify;
    text-align-last: justify;
  }

  /* following pages header */
  .mini-name {
    position: absolute;
    left: 0; top: 24px;
    width: 113px; height: 16px;
    background: var(--violet);
    clip-path: polygon(0 0, 100% 0, 93% 100%, 0 100%);
    color: var(--white);
    font-size: 8.4px;
    line-height: 16px;
    padding-left: 25px;
    white-space: nowrap;
  }
  .mini-services {
    position: absolute;
    left: 111px; top: 24px;
    width: 371px; height: 16px;
    background: var(--slate);
    clip-path: polygon(8px 0, 100% 0, 100% 100%, 0 100%);
    color: #ececec;
    font-size: 6.9px;
    line-height: 16px;
    padding-left: 30px;
    white-space: nowrap;
  }
</style>
</head>
<body>
  <section class="sheet sheet--first">
    <div class="name-band">
      <div class="name-band__name">VALMOR KELLER</div>
      <div class="name-band__title">eidg. dipl. Malermeister</div>
    </div>
    <div class="contact-band">
      Lindenweg 7, 8805 Richterswil<br>
      <b>Telefon:</b> 044 583 61 47 · <b>Fax:</b> 044 583 61 37<br>
      <b>Natel:</b> 079 512 40 63 · <b>Email:</b> gutachten@valmorkeller.example
    </div>
    <p class="services">GUTACHTEN EXPERTISEN • DEVISIERUNGEN • FARBBERATUNGEN • DEKORATIVE GESTALTUNGEN</p>
  </section>

  <section class="sheet sheet--follow">
    <div class="mini-name">VALMOR KELLER</div>
    <div class="mini-services">GUTACHTEN EXPERTISEN &nbsp;•&nbsp; DEVISIERUNGEN &nbsp;•&nbsp; FARBBERATUNGEN &nbsp;•&nbsp; DEKORATIVE GESTALTUNGEN</div>
  </section>
</body>
</html>
```